Energy Company needs a Business Card Design

We need a business card design for a new company based in Singapore called Tarn Energy. Tarn Energy is a producer of renewable energies largely for the biofuels market. Sourced entirely from sustainable resources, Tarn Energy aims to be a fully integrated oil company operating in 100% sustainable way. We would like to see designs that use the same colours as the attached file.

Industry/Entity Type

Business

```html
<!DOCTYPE html>
<html lang="en">
<head>
<meta charset="utf-8">
<title>Tarn Energy – Business Card</title>
<link rel="stylesheet" href="https://fonts.googleapis.com/css2?family=Questrial&display=swap">
<style>
  :root {
    --paper: #ffffff;
    --ink: #111111;
    --brand-grey: #939396;
    --brand-green: #7dc242;
  }
  html, body {
    margin: 0;
    padding: 0;
    overflow: hidden;
    background: var(--paper);
  }
  .card {
    position: relative;
    width: 791px;
    height: 1200px;
    background: var(--paper);
    font-family: "Questrial", "Century Gothic", sans-serif;
    color: var(--ink);
    overflow: hidden;
  }
  .brand {
    position: absolute;
    left: 48px;
    top: 240px;
    display: flex;
    align-items: center;
    gap: 22px;
  }
  .brand-dot {
    display: block;
    width: 64px;
    height: 64px;
  }
  .brand-name {
    font-size: 58px;
    line-height: 1;
    color: var(--brand-grey);
    font-weight: 400;
    letter-spacing: 0.5px;
  }
  .person {
    position: absolute;
    left: 212px;
    top: 474px;
  }
  .person-name {
    margin: 0;
    font-size: 60px;
    font-weight: 400;
    line-height: 1;
    letter-spacing: 1px;
  }
  .person-details {
    margin: 10px 0 0;
    padding: 0;
    list-style: none;
    font-size: 28px;
    line-height: 38px;
  }
  .company-details {
    position: absolute;
    left: 0;
    right: 0;
    top: 972px;
    margin: 0;
    padding: 0;
    list-style: none;
    text-align: center;
    font-size: 28px;
    line-height: 33.5px;
  }
</style>
</head>
<body>
  <main class="card">
    <div class="brand">
      <svg class="brand-dot" viewBox="0 0 64 64" aria-hidden="true">
        <circle cx="32" cy="32" r="32" fill="var(--brand-green)"/>
      </svg>
      <span class="brand-name">Tarn Energy</span>
    </div>

    <section class="person">
      <h1 class="person-name">NAME</h1>
      <ul class="person-details">
        <li class="designation">Designation</li>
        <li class="did">DID: +65 61234567</li>
        <li class="mobile">Mobile: +65 81234567</li>
        <li class="email">Email: abc@tarn.com.sg</li>
      </ul>
    </section>

    <ul class="company-details">
      <li>123 Street Name, Building Name,</li>
      <li>Singapore 123456</li>
      <li>Office Main Line: 61234567</li>
      <li>Office Main Email: tarn@tarn.com.sg</li>
      <li>*services and products here*</li>
    </ul>
  </main>
</body>
</html>
```